'Wedding Business" Business Card Design

dj services for weddings and parties, uplighting, event planning, day of coordination for weddings, photography for weddings and other events.

Would like raised print and metallic also if possible. Elegant design, yet modern. This is a wedding business and should describe our goals and main services - DJ/lighting, wedding and event planning, photography. slogan "Simply Incredible, Incredibly simple" or "Your Dreams. Our Experience. The Perfect Match" Our goal is to provide multiple services to make it easier for the bride and groom almost like a one stop shop. Feel free to use the slogan or leave it out , we just want to really stand out against the competition. You can also get more info on our website www.brightlanestudios.com - we are working to get the brightlanenc.com site pointed to our current site!

there should be 2 files attached, if they did not go through please email events@brightlanenc.com or brightlanestudios@mailbox.test
Updates

Thank you all for your help, we have decided what we like but would like to make some changes, we need to order these asap so please let us know if you can help.

Reason: Wasn't able to pick it out in time! So Sorry but we know what we want!!

Industry/Entity Type

Business

Contact Information for Business Card

Marcus and Leona Whitcombe
555-318-2047
555-720-4861
Bright Lane Studios, Events, & Photography
EMAIL:Events@BrightLaneNC.com
www.brightlanenc.com

```html
<!DOCTYPE html>
<html lang="en">
<head>
<meta charset="utf-8">
<title>Bright Lane Studios — Business Card</title>
<link href="https://fonts.googleapis.com/css2?family=Playball&family=Tinos:wght@400;700&display=swap" rel="stylesheet">
<style>
  :root {
    --stage: #e8e5de;
    --cream: #ede8d6;
    --gold: #b48a1c;
    --gold-light: #f0e3a4;
    --gold-mid: #e6d27e;
    --navy: #232447;
    --ink: #3a3650;
    --seal: #111116;
    --seal-rim: #d9d9dc;
  }
  * { box-sizing: border-box; margin: 0; padding: 0; }
  html, body { width: 1200px; height: 1000px; overflow: hidden; }
  body { background: var(--stage); position: relative; font-family: "Tinos", "Times New Roman", serif; }

  .card {
    position: absolute; left: 240px; width: 720px; height: 412px;
    background: var(--cream); overflow: hidden;
    box-shadow: 0 6px 18px rgba(0,0,0,0.18);
  }
  .card--front { top: 62px; }
  .card--back { top: 526px; }
  .card__art { position: absolute; inset: 0; width: 100%; height: 100%; }

  .seal-name {
    position: absolute; width: 84px; text-align: center;
    font-family: "Tinos", "Times New Roman", serif; font-weight: 700;
    font-size: 15px; line-height: 1.1; color: var(--cream);
  }

  .slogan {
    position: absolute; left: 180px; top: 112px;
    font-family: "Playball", cursive;
    color: var(--gold); font-size: 32px; line-height: 1.15;
  }
  .slogan__line { display: block; }
  .slogan__line--two { padding-left: 64px; }

  .contact { position: absolute; left: 58px; top: 160px; }
  .contact__names { font-family: "Playball", cursive; font-weight: 400; color: var(--gold); font-size: 38px; line-height: 1.1; margin-bottom: 12px; }
  .contact__phones { margin-bottom: 4px; }
  .contact__phone { font-weight: 700; color: var(--navy); font-size: 25px; line-height: 1.25; }
  .contact__line { color: var(--ink); font-size: 17px; line-height: 1.55; }
</style>
</head>
<body>

  <section class="card card--front">
    <svg class="card__art" viewBox="0 0 720 412">
      <defs>
        <linearGradient id="dressTone" x1="0" y1="0" x2="1" y2="1">
          <stop offset="0" stop-color="#d9b53c"/>
          <stop offset="0.45" stop-color="#c98a2a"/>
          <stop offset="0.75" stop-color="#a9ad6c"/>
          <stop offset="1" stop-color="#a8542a"/>
        </linearGradient>
        <radialGradient id="ringTone" cx="0.5" cy="0.4" r="0.6">
          <stop offset="0" stop-color="#f6e08a"/>
          <stop offset="1" stop-color="#b0851e"/>
        </radialGradient>
      </defs>
      <rect width="720" height="412" fill="var(--cream)" role="img" aria-label="Light swirl and heart pattern"/>
      <path d="M560 0 C700 90 720 200 720 260 L720 0 Z" fill="var(--gold-mid)"/>
      <path d="M600 0 C705 80 720 160 720 200 L720 0 Z" fill="var(--gold-light)"/>
      <g class="ribbon">
        <rect x="508" y="0" width="6" height="200" fill="var(--navy)"/>
        <rect x="526" y="0" width="6" height="200" fill="var(--navy)"/>
      </g>
      <circle cx="520" cy="78" r="52" fill="var(--seal-rim)"/>
      <circle cx="520" cy="78" r="44" fill="var(--seal)"/>
      <ellipse cx="590" cy="222" rx="56" ry="30" fill="url(#ringTone)" role="img" aria-label="Pair of gold wedding rings"/>
      <path d="M30 412 V250 Q30 210 70 210 H130 C250 240 380 300 470 412 Z"
            fill="url(#dressTone)" role="img" aria-label="Illustration of a bride with a bouquet in a flowing dress of autumn petals"/>
    </svg>
    <span class="seal-name" style="left:478px; top:60px;">Bright Lane</span>
    <p class="slogan">
      <span class="slogan__line">Simply Incredible,</span>
      <span class="slogan__line slogan__line--two">Incredibly simple</span>
    </p>
  </section>

  <section class="card card--back">
    <svg class="card__art" viewBox="0 0 720 412">
      <defs>
        <radialGradient id="ringToneBack" cx="0.5" cy="0.4" r="0.6">
          <stop offset="0" stop-color="#f6e08a"/>
          <stop offset="1" stop-color="#b0851e"/>
        </radialGradient>
      </defs>
      <rect width="720" height="412" fill="var(--cream)" role="img" aria-label="Light swirl and heart pattern"/>
      <path d="M600 0 C720 120 680 330 140 412 L720 412 L720 0 Z" fill="var(--gold-mid)"/>
      <path d="M650 0 C735 140 690 340 330 412 L720 412 L720 0 Z" fill="var(--gold-light)"/>
      <g class="ribbon">
        <rect x="558" y="0" width="6" height="200" fill="var(--navy)"/>
        <rect x="576" y="0" width="6" height="200" fill="var(--navy)"/>
      </g>
      <circle cx="570" cy="78" r="52" fill="var(--seal-rim)"/>
      <circle cx="570" cy="78" r="44" fill="var(--seal)"/>
      <ellipse cx="650" cy="210" rx="52" ry="30" fill="url(#ringToneBack)" role="img" aria-label="Pair of gold wedding rings"/>
    </svg>
    <span class="seal-name" style="left:528px; top:60px;">Bright Lane</span>
    <div class="contact">
      <h1 class="contact__names">Marcus and Leona Whitcombe</h1>
      <div class="contact__phones">
        <p class="contact__phone">555-318-2047</p>
        <p class="contact__phone">555-720-4861</p>
      </div>
      <p class="contact__line">Bright Lane Studios, Events, &amp; Photography</p>
      <p class="contact__line">Events@BrightLaneNC.com</p>
      <p class="contact__line">www.brightlanenc.com</p>
    </div>
  </section>

</body>
</html>
```